Tech business card design

We need an amazing business card design for our new business 'Brakka' a marketing tech startup based in Sydney, Australia. We provide an online marketplace for businesses to search and buy advertising media, connect with service providers and learn more about marketing. We wish to communicate 'cool tech', reliability and professionalism and design based around our logo.

Target Market(s)

Business Owners

Contact Information for Business Card

Name
Position
Email Address
Website
Phone Number

Font styles to use
Other font styles liked:
• Avenir & Avenir Next

Colors

Designer to choose colors to be used in the design.

```html
<!DOCTYPE html>
<html lang="en">
<head>
<meta charset="utf-8">
<title>Brakka business card</title>
<link href="https://fonts.googleapis.com/css2?family=Roboto:wght@400;500;700&display=swap" rel="stylesheet">
<style>
  :root {
    --backdrop: #24234b;
    --card-navy: #1d1c47;
    --paper: #efefef;
    --accent-blue: #4a86c8;
    --text-white: #ffffff;
    --rim-grey: #b9b9bf;
  }
  html, body {
    margin: 0;
    padding: 0;
    width: 1200px;
    height: 986px;
    overflow: hidden;
    background: var(--backdrop);
    font-family: "Roboto", sans-serif;
  }
  .canvas {
    position: relative;
    width: 1200px;
    height: 986px;
  }
  .card {
    position: absolute;
    left: 342px;
    width: 516px;
    height: 296px;
    border-radius: 24px;
    background: var(--card-navy);
    box-shadow: 0 18px 36px rgba(0, 0, 0, 0.35);
    overflow: hidden;
  }
  .card--front { top: 160px; }
  .card--back { top: 530px; }
  .front-shape {
    position: absolute;
    inset: 0;
  }
  .contact-block {
    position: absolute;
    left: 36px;
    top: 74px;
    color: var(--text-white);
  }
  .person-name {
    margin: 0;
    font-size: 21px;
    font-weight: 500;
    color: var(--accent-blue);
    line-height: 24px;
  }
  .person-role {
    margin: 0;
    font-size: 14.5px;
    font-weight: 400;
    line-height: 18px;
  }
  .address {
    margin: 20px 0 0;
    font-size: 12.5px;
    line-height: 17px;
    font-style: normal;
  }
  .contact-list {
    list-style: none;
    margin: 17px 0 0;
    padding: 0;
    font-size: 12.5px;
    line-height: 17.5px;
  }
  .contact-list li {
    display: flex;
    align-items: center;
    gap: 6px;
  }
  .contact-icon {
    width: 11px;
    height: 11px;
    fill: var(--accent-blue);
    flex: none;
  }
  .wordmark {
    position: absolute;
    margin: 0;
    font-family: "Roboto", sans-serif;
    font-weight: 700;
    letter-spacing: -1px;
    line-height: 1;
  }
  .wordmark--front {
    left: 288px;
    top: 118px;
    font-size: 52px;
    color: var(--card-navy);
  }
  .wordmark--back {
    left: 0;
    right: 0;
    top: 104px;
    text-align: center;
    font-size: 66px;
    color: var(--text-white);
  }
</style>
</head>
<body>
<div class="canvas">

  <section class="card card--front">
    <svg class="front-shape" width="516" height="296" viewBox="0 0 516 296" aria-hidden="true">
      <circle cx="394" cy="148" r="162" fill="var(--rim-grey)"/>
      <circle cx="400" cy="148" r="161" fill="var(--card-navy)"/>
      <circle cx="406" cy="148" r="160" fill="var(--paper)"/>
    </svg>

    <div class="contact-block">
      <h1 class="person-name">Marcus Ellery</h1>
      <p class="person-role">Managing Director</p>
      <address class="address">Level 2, 17 Tallow Lane<br>Carrington, NSW 2000</address>
      <ul class="contact-list">
        <li>
          <svg class="contact-icon" viewBox="0 0 24 24"><path d="M6.6 10.8a15.1 15.1 0 0 0 6.6 6.6l2.2-2.2c.3-.3.7-.4 1-.2 1.1.4 2.3.6 3.6.6.6 0 1 .4 1 1V20c0 .6-.4 1-1 1A17 17 0 0 1 3 4c0-.6.4-1 1-1h3.5c.6 0 1 .4 1 1 0 1.3.2 2.5.6 3.6.1.3 0 .7-.2 1z"/></svg>
          <span>123 456 7890</span>
        </li>
        <li>
          <svg class="contact-icon" viewBox="0 0 24 24"><path d="M2 5h20v2l-10 6L2 7z M2 9l10 6 10-6v10H2z"/></svg>
          <span>info@yourwebsite.com</span>
        </li>
        <li>
          <svg class="contact-icon" viewBox="0 0 24 24"><path d="M12 2a10 10 0 1 0 0 20 10 10 0 0 0 0-20zm6.9 6h-3a15 15 0 0 0-1.3-4A8 8 0 0 1 18.9 8zM12 4c.8 1.2 1.5 2.5 1.9 4h-3.8c.4-1.5 1.1-2.8 1.9-4zM4.3 14a8 8 0 0 1 0-4h3.4a16 16 0 0 0 0 4zm.8 2h3a15 15 0 0 0 1.3 4A8 8 0 0 1 5.1 16zm3-8h-3a8 8 0 0 1 4.3-4 15 15 0 0 0-1.3 4zM12 20c-.8-1.2-1.5-2.5-1.9-4h3.8c-.4 1.5-1.1 2.8-1.9 4zm2.3-6H9.7a14 14 0 0 1 0-4h4.6a14 14 0 0 1 0 4zm.3 6a15 15 0 0 0 1.3-4h3a8 8 0 0 1-4.3 4zm1.7-6a16 16 0 0 0 0-4h3.4a8 8 0 0 1 0 4z"/></svg>
          <span>www.yourwebsite.com</span>
        </li>
      </ul>
    </div>

    <p class="wordmark wordmark--front">Brakka</p>
  </section>

  <section class="card card--back">
    <p class="wordmark wordmark--back">Brakka</p>
  </section>

</div>
</body>
</html>
```